Building Company Business Card Design

I am looking to get a business card designed for my Building Company. Please find the logo attached.

Industry/Entity Type

Business

Contact Information for Business Card

Mobile 0472 913 046
Email admin@tarrowconstructworks.com.au
Website www.tarrowconstructworks.com.au

Colors
0255a3

```html
<!DOCTYPE html>
<html lang="en">
<head>
<meta charset="utf-8">
<title>Tarrow Construct Works – Business Card</title>
<link rel="stylesheet" href="https://fonts.googleapis.com/css2?family=Arimo:wght@400;700&display=swap">
<style>
  :root {
    --brand-blue: #1055a3;
    --deep-blue: #0d4d97;
    --sky-blue-soft: #b9cde6;
    --steel-grey: #6d6e71;
    --light-grey: #8a8b8e;
    --grey-soft: #d9dadc;
    --paper: #ffffff;
    --frame: #3a3a3a;
    --bullet-orange: #f39a1f;
  }
  * { margin: 0; padding: 0; box-sizing: border-box; }
  html, body { width: 1200px; height: 450px; overflow: hidden; background: var(--paper); }
  body { position: relative; font-family: "Arimo", Arial, sans-serif; }

  .card {
    position: absolute;
    top: 70px;
    width: 515px;
    height: 315px;
    background: var(--paper);
    border: 1px solid var(--frame);
    overflow: hidden;
  }
  .card--front { left: 66px; }
  .card--back { left: 624px; }

  .front-art { position: absolute; inset: 0; }

  .front-skyline {
    position: absolute;
    left: 0; right: 0;
    top: 76px;
    height: 118px;
    background: linear-gradient(to bottom, var(--paper) 0%, var(--sky-blue-soft) 22%, var(--brand-blue) 62%, var(--brand-blue) 100%);
  }

  .wordmark {
    position: absolute;
    font-weight: 700;
    color: var(--brand-blue);
    text-transform: uppercase;
    line-height: 1.05;
    white-space: nowrap;
    display: flex;
    align-items: center;
  }
  .wordmark__square {
    display: inline-block;
    flex: none;
    background: var(--brand-blue);
  }
  .card--front .wordmark { left: 20px; top: 36px; font-size: 17px; gap: 8px; }
  .card--front .wordmark__square { width: 14px; height: 14px; }
  .card--back .wordmark {
    left: 0; right: 0; top: 110px;
    justify-content: center;
    font-size: 25px; gap: 12px;
  }
  .card--back .wordmark__square { width: 20px; height: 20px; }

  .holder {
    position: absolute;
    left: 24px;
    top: 238px;
    color: var(--paper);
  }
  .holder__name { font-size: 16px; letter-spacing: 0.2px; text-transform: uppercase; }
  .holder__role { font-size: 14.5px; margin-top: 7px; }

  .contacts {
    position: absolute;
    left: 249px;
    top: 240px;
    list-style: none;
    color: var(--paper);
    font-size: 11.6px;
  }
  .contacts li { margin-bottom: 6px; white-space: nowrap; }
  .contacts li::before {
    content: "•";
    color: var(--bullet-orange);
    margin-right: 4px;
  }

  .back-skyline {
    position: absolute;
    left: 0; right: 0; bottom: 0;
    height: 72px;
    background: linear-gradient(to bottom, var(--paper) 0%, var(--grey-soft) 25%, var(--light-grey) 60%, var(--steel-grey) 100%);
  }
</style>
</head>
<body>

  <section class="card card--front">
    <div class="front-skyline" role="img" aria-label="Blue city skyline silhouette of office towers"></div>
    <svg class="front-art" width="515" height="315" viewBox="0 0 515 315" aria-hidden="true">
      <path d="M0 208 Q257 190 515 212 L515 315 L0 315 Z" fill="var(--deep-blue)"/>
      <path d="M0 202 Q257 184 515 206 L515 212 Q257 190 0 208 Z" fill="var(--paper)"/>
      <path d="M0 196 Q257 178 515 200 L515 206 Q257 184 0 202 Z" fill="var(--light-grey)"/>
      <path d="M0 191 Q257 173 515 195 L515 200 Q257 178 0 196 Z" fill="var(--paper)"/>
      <path d="M0 186 Q257 168 515 190 L515 195 Q257 173 0 191 Z" fill="var(--brand-blue)"/>
    </svg>

    <div class="wordmark"><span class="wordmark__square"></span>Tarrow Construct Works</div>

    <div class="holder">
      <p class="holder__name">Dara Quinlan Vu</p>
      <p class="holder__role">General Director</p>
    </div>

    <ul class="contacts">
      <li>Mobile: 0472 913 046</li>
      <li>Email: admin@tarrowconstructworks.com.au</li>
      <li>Website: www.tarrowconstructworks.com.au</li>
    </ul>
  </section>

  <section class="card card--back">
    <div class="wordmark"><span class="wordmark__square"></span>Tarrow Construct Works</div>
    <div class="back-skyline" role="img" aria-label="Grey city skyline silhouette along the bottom edge"></div>
  </section>

</body>
</html>
```